Business Cards for a Junk Removal Company

Hello,
We are looking to have business cards designed that are simple, bold, easy to read, and right to the point. Please see the attachments for our logo files. We want the card to be yellow on both sides ( Color code Yellow: #FFE01B). The logo text font is (Rockstar Extra Bold) and this is also in the files attached. Please make the text black for the logo. On the back side of the card, you can use white and black for text. Thank you in advance for your hard work!

Front of card-
Harbor Haul Away (logo)
Back of card-
Harbor Haul Away
Donate - Recycle - Dispose
555-271-8093
www.harborhaulaway.example
info@harborhaulaway.example

Industry/Entity Type

Junk removal

Contact Information for Business Card

FRONT OF CARD- Harbor Haul Away (logo) BACK OF CARD- Harbor Haul Away Donate - Recycle - Dispose 555-271-8093 www.harborhaulaway.example info@harborhaulaway.example

Font styles to use
Other font styles liked:
• Rockstar Extra Bold

Colors
FFF300
FFF600
FEFA6F
FFFEC7
FFFEE8

Requirements
Must have
• Must have color code Yellow: #FFE01B for the background of front and back of the card

```html
<!DOCTYPE html>
<html lang="en">
<head>
<meta charset="utf-8">
<title>Harbor Haul Away – Business Cards</title>
<link rel="stylesheet" href="https://fonts.googleapis.com/css2?family=Anton&display=swap">
<style>
  :root {
    --card-yellow: #FFE01B;
    --ink: #0a0a0a;
    --backdrop: #e2e2e2;
    --paper-white: #ffffff;
  }
  * { box-sizing: border-box; margin: 0; padding: 0; }
  html, body {
    width: 1200px;
    height: 900px;
    overflow: hidden;
    background: var(--backdrop);
    font-family: "Anton", "Arial Narrow", sans-serif;
    color: var(--ink);
  }
  .stage { position: relative; width: 1200px; height: 900px; }
  .card {
    position: absolute;
    top: 217px;
    width: 308px;
    height: 500px;
    background: var(--card-yellow);
  }
  .card--front { left: 280px; border-radius: 0 72px 0 72px; }
  .card--back  { left: 617px; border-radius: 72px 0 72px 0; }

  .brand {
    position: absolute;
    left: 0; right: 0;
    text-align: center;
    line-height: 1;
  }
  .card--front .brand { top: 126px; }
  .card--back .brand  { top: 116px; }
  .brand__main {
    display: block;
    font-size: 54px;
    letter-spacing: 0.5px;
  }
  .brand__sub {
    display: block;
    margin-top: 8px;
    font-size: 22px;
    letter-spacing: 5px;
  }

  .call-icon {
    position: absolute;
    top: 290px;
    left: 122px;
    width: 64px;
    height: 64px;
  }
  .front-phone {
    position: absolute;
    top: 366px;
    left: 0; right: 0;
    text-align: center;
    font-size: 30px;
    letter-spacing: 0.5px;
  }

  .tagline {
    position: absolute;
    top: 262px;
    left: 0; right: 0;
    text-align: center;
    font-size: 18px;
    letter-spacing: 0.3px;
  }

  .contact-list {
    position: absolute;
    top: 361px;
    left: 32px;
    list-style: none;
  }
  .contact-list li {
    display: flex;
    align-items: center;
    height: 19.5px;
    font-size: 13.5px;
    letter-spacing: 0.2px;
    text-transform: uppercase;
  }
  .contact-list svg {
    width: 12px;
    height: 12px;
    margin-right: 9px;
    flex: none;
  }
</style>
</head>
<body>
<main class="stage">

  <section class="card card--front" aria-label="Card front">
    <div class="brand">
      <span class="brand__main">HARBOR</span>
      <span class="brand__sub">HAUL AWAY</span>
    </div>
    <svg class="call-icon" viewBox="0 0 64 64" aria-hidden="true">
      <circle cx="32" cy="32" r="32" fill="var(--ink)"/>
      <path d="M22 18c1.5-1.5 3.5-1.3 4.6.3l3 4.3c.9 1.3.7 3-.5 4l-2 1.7c1.6 3.6 4.3 6.4 7.8 8l1.7-2c1-1.2 2.7-1.4 4-.5l4.3 3c1.6 1.1 1.8 3.1.3 4.6l-2 2c-2 2-5 2.3-8 .8-7.5-3.8-13.3-9.6-17-17-1.5-3-1.2-6 .8-8z" fill="var(--paper-white)"/>
      <path d="M35 20a10 10 0 0 1 9 9M36 14a16 16 0 0 1 14 14" fill="none" stroke="var(--paper-white)" stroke-width="2.6" stroke-linecap="round"/>
    </svg>
    <p class="front-phone">555-271-8093</p>
  </section>

  <section class="card card--back" aria-label="Card back">
    <div class="brand">
      <span class="brand__main">HARBOR</span>
      <span class="brand__sub">HAUL AWAY</span>
    </div>
    <p class="tagline">DONATE - RECYCLE - DISPOSE</p>
    <ul class="contact-list">
      <li>
        <svg viewBox="0 0 12 12" aria-hidden="true"><path d="M2.5 1.2c.5-.5 1.1-.4 1.4.1l.9 1.3c.3.4.2.9-.2 1.2l-.5.5c.5 1.1 1.3 1.9 2.4 2.4l.5-.5c.3-.4.8-.5 1.2-.2l1.3.9c.5.3.6.9.1 1.4l-.6.6c-.6.6-1.5.7-2.4.2C4.3 8 2.6 6.3 1.5 4 1 3.2 1.1 2.3 1.7 1.7z" fill="var(--ink)"/></svg>
        555-271-8093
      </li>
      <li>
        <svg viewBox="0 0 12 12" aria-hidden="true"><circle cx="6" cy="6" r="5" fill="none" stroke="var(--ink)" stroke-width="1.2"/><path d="M1 6h10M6 1c-2.2 2.8-2.2 7.2 0 10M6 1c2.2 2.8 2.2 7.2 0 10" fill="none" stroke="var(--ink)" stroke-width="1"/></svg>
        www.harborhaulaway.example
      </li>
      <li>
        <svg viewBox="0 0 12 12" aria-hidden="true"><rect x="0.6" y="2.2" width="10.8" height="7.6" fill="var(--ink)"/><path d="M1 2.8l5 3.8 5-3.8" fill="none" stroke="var(--card-yellow)" stroke-width="1"/></svg>
        info@harborhaulaway.example
      </li>
    </ul>
  </section>

</main>
</body>
</html>
```